New Zealand Export company needs business cards

We need new business cards to match our new logo for a company based in New Zealand who deal specifically with the Pacific Islands. We source, consolidate and ship products out of New Zealand to the Pacific Islands. Will attach our old ones and also new logo.
Would like the Islands we deal with and the areas of work we have access to, to be included on the business cards.

Contact Information for Business Card

T +64 9 381 5047
F +64 9 381 6620
12-18 Marlow Lane, Drury, 2113
PO Box 862, Drury, Auckland 2247, New Zealand
www.kestaltrade.co.nz
E sales@kestaltrade.co.nz

Font styles to use
Sans Serif

Colors
85abd2
33a6d7
ffffff

Requirements
Must have
• A company of WMB

```html
<!DOCTYPE html>
<html lang="en">
<head>
<meta charset="utf-8">
<title>Kestal Trade – Business Card</title>
<link rel="stylesheet" href="https://fonts.googleapis.com/css2?family=Montserrat:wght@700&family=Open+Sans:wght@400;600&display=swap">
<style>
  :root {
    --brand-blue: #00a8dc;
    --brand-navy: #0b5ca8;
    --card-white: #ffffff;
    --backdrop: #c9ccb2;
  }
  * { box-sizing: border-box; margin: 0; padding: 0; }
  html, body { width: 1200px; height: 900px; overflow: hidden; }
  body {
    background: var(--backdrop);
    font-family: "Open Sans", sans-serif;
    display: flex; align-items: center; justify-content: center;
  }
  .card {
    position: relative;
    width: 1000px; height: 572px;
    background: var(--card-white);
    overflow: hidden;
    box-shadow: 0 12px 30px rgba(0,0,0,.18);
  }
  .panel-contact {
    position: absolute; left: 0; top: 0;
    width: 62%; height: 58%;
    background: var(--brand-blue);
  }
  .panel-contact-lower {
    position: absolute; left: 0; top: 58%;
    width: 43%; height: 26%;
    background: var(--brand-blue);
  }
  .edge-strip {
    position: absolute; right: 0; top: 60%;
    width: 3.6%; height: 40%;
    background: var(--brand-blue);
  }
  .icon-tab {
    position: absolute; left: 1.2%;
    width: 6.8%; height: 8%;
    background: var(--brand-navy);
    display: flex; align-items: center; justify-content: center;
  }
  .icon-tab svg { width: 30px; height: 30px; fill: var(--card-white); }
  .tab-address { top: 21%; }
  .tab-phone   { top: 45%; }
  .tab-email   { top: 65%; }
  .contact-block {
    position: absolute; left: 10.5%;
    color: var(--card-white);
    font-size: 24px; line-height: 1.55;
  }
  .contact-address { top: 13%; }
  .contact-phone   { top: 41%; }
  .contact-email   { top: 62%; }
  .person {
    position: absolute; left: 65%; top: 7%;
    color: var(--brand-navy);
  }
  .person-name {
    font-family: "Montserrat", sans-serif;
    font-weight: 700; font-size: 28px; letter-spacing: 4px;
  }
  .person-title { font-size: 24px; letter-spacing: 4px; }
  .brand {
    position: absolute; left: 46%; top: 64%;
    display: flex; align-items: center; gap: 18px;
  }
  .brand-square {
    width: 54px; height: 54px; background: var(--brand-navy);
  }
  .brand-name {
    font-family: "Open Sans", sans-serif;
    font-weight: 600; font-size: 48px; letter-spacing: 3px;
    color: var(--brand-navy);
  }
  .website {
    position: absolute; left: 47%; top: 87%;
    font-size: 24px; letter-spacing: 6px;
    color: var(--brand-navy);
  }
</style>
</head>
<body>
  <main class="card">
    <div class="panel-contact"></div>
    <div class="panel-contact-lower"></div>
    <div class="edge-strip"></div>

    <div class="icon-tab tab-address">
      <svg viewBox="0 0 24 24" aria-hidden="true"><path d="M12 3 2 12h3v8h5v-5h4v5h5v-8h3z"/></svg>
    </div>
    <div class="icon-tab tab-phone">
      <svg viewBox="0 0 24 24" aria-hidden="true"><path d="M6.6 10.8a15 15 0 0 0 6.6 6.6l2.2-2.2a1 1 0 0 1 1-.25 11.4 11.4 0 0 0 3.6.57 1 1 0 0 1 1 1V20a1 1 0 0 1-1 1A17 17 0 0 1 3 4a1 1 0 0 1 1-1h3.5a1 1 0 0 1 1 1c0 1.25.2 2.45.57 3.57a1 1 0 0 1-.25 1z"/></svg>
    </div>
    <div class="icon-tab tab-email">
      <svg viewBox="0 0 24 24" aria-hidden="true"><path d="M2 5h20v14H2z" fill="none" stroke="#fff" stroke-width="2"/><path d="M2 5l10 8 10-8" fill="none" stroke="#fff" stroke-width="2"/></svg>
    </div>

    <p class="contact-block contact-address">
      12-18 Marlow Lane, Drury, 2113<br>
      PO Box 862, Drury, Auckland 2247,<br>
      New Zealand
    </p>
    <p class="contact-block contact-phone">
      T +64 9 381 5047<br>
      F +64 9 381 6620
    </p>
    <p class="contact-block contact-email">E sales@kestaltrade.co.nz</p>

    <div class="person">
      <p class="person-name">LENA HARWOOD</p>
      <p class="person-title">Sales Manager</p>
    </div>

    <div class="brand">
      <span class="brand-square"></span>
      <span class="brand-name">KESTAL TRADE</span>
    </div>

    <p class="website">www.kestaltrade.co.nz</p>
  </main>
</body>
</html>
```